RIDEVOLT CYCLES Company

I need a RIDEVOLT CYCLES site for pre-orders, 3-4 models, multiple colors per order. The bikes are electric bikes, company logo color scheme has red. Maybe a countdown to a date when pre-order will close. I also want to incorporate a deposit style system for the pre-order with the balance due on shipping.

Coding

```html
<!DOCTYPE html>
<html lang="en">
<head>
<meta charset="utf-8">
<title>Ridevolt Cycles – Electric Bicycle Pre-Orders</title>
<link href="https://fonts.googleapis.com/css2?family=Nunito+Sans:wght@400;600;700;800;900&family=Mulish:wght@400;500;600;700&display=swap" rel="stylesheet">
<style>
:root{
  --red:#e8161b;
  --ink:#151515;
  --text:#3a3a3a;
  --muted:#666;
  --card:#f4f3f3;
  --soft:#f3f2f2;
  --line:#d9d9d9;
  --black:#000;
  --white:#fff;
}
*{margin:0;padding:0;box-sizing:border-box}
html,body{width:1200px;height:4637px;overflow:hidden}
body{font-family:"Mulish",sans-serif;color:var(--text);background:var(--white);position:relative}
h1,h2,h3,h4{font-family:"Nunito Sans",sans-serif}

/* header */
.site-header{position:absolute;top:0;left:0;width:1200px;height:80px;background:var(--white)}
.brand-name{position:absolute;font-family:"Mulish",sans-serif;font-weight:700;white-space:nowrap}
.site-header .brand-name{left:131px;top:24px;font-size:24px;color:var(--ink)}
.main-nav{position:absolute;top:32px;left:456px;font-family:"Nunito Sans",sans-serif;font-size:13px;font-weight:700;color:var(--ink)}
.main-nav span{position:absolute;white-space:nowrap}
.main-nav .active{color:var(--red)}
.main-nav .active::after{content:"";position:absolute;left:0;right:0;top:23px;height:2px;background:var(--red)}
.cart{position:absolute;left:1036px;top:28px}
.cart-badge{position:absolute;left:1052px;top:22px;width:14px;height:14px;border-radius:50%;background:var(--red);color:#fff;font-size:9px;font-weight:700;text-align:center;line-height:14px}

/* hero */
.hero{position:absolute;top:80px;left:0;width:1200px;height:634px;background:linear-gradient(100deg,#5a5138 0%,#6b6141 25%,#8a7a5a 45%,#6a5d45 65%,#3f3a2c 100%)}
.hero-title{position:absolute;left:570px;top:114px;width:520px;font-size:40px;line-height:48px;font-weight:900;color:#fff}
.hero-date{position:absolute;left:576px;top:284px;font-size:31px;font-weight:500;color:#fff}
.countdown{position:absolute;left:575px;top:340px;display:flex;gap:4px}
.digit{width:44px;height:58px;background:linear-gradient(#3b3b3b 50%,#262626 50%);border-radius:4px;color:#fff;font-family:"Nunito Sans",sans-serif;font-size:42px;font-weight:600;text-align:center;line-height:58px}
.digit.last{color:var(--red)}
.count-labels{position:absolute;left:575px;top:406px;width:390px;font-size:8px;color:#eee;letter-spacing:.5px}
.count-labels span{position:absolute;width:96px;text-align:center}
.btn{display:inline-block;background:var(--red);color:#fff;font-family:"Nunito Sans",sans-serif;font-weight:800;text-align:center}
.hero .btn{position:absolute;left:575px;top:455px;width:164px;height:46px;line-height:46px;font-size:19px}
.dots{position:absolute;left:557px;top:589px;display:flex;gap:8px}
.dots i{width:9px;height:9px;border-radius:50%;background:#fff}
.dots i.on{background:var(--red)}

.section-title{position:absolute;left:0;width:1200px;text-align:center;font-size:33px;font-weight:900;color:var(--ink)}
.rule{position:absolute;width:44px;height:3px;background:var(--red)}

/* products */
.product{position:absolute;width:454px;height:585px;background:var(--card);text-align:center}
.product .photo{position:absolute;left:57px;top:30px;width:340px;height:290px;border-radius:4px}
.product h3{position:absolute;top:344px;width:100%;font-size:19px;font-weight:800;color:var(--ink)}
.product .price{position:absolute;top:378px;width:100%;font-family:"Nunito Sans",sans-serif;font-size:20px;font-weight:800;color:var(--red)}
.swatches{position:absolute;top:422px;left:0;width:100%;display:flex;justify-content:center;align-items:center;gap:4px;font-family:"Nunito Sans",sans-serif;font-size:11px;font-weight:700;color:var(--ink)}
.swatches b{margin-right:8px}
.swatches i{width:8px;height:8px;border-radius:50%}
.product p{position:absolute;top:450px;left:43px;width:368px;font-size:13px;line-height:21px;color:var(--text)}
.product .btn{position:absolute;top:512px;left:165px;width:118px;height:33px;line-height:33px;font-size:13px}

/* bands */
.welcome{position:absolute;top:2104px;left:0;width:1200px;height:497px;background:linear-gradient(90deg,#1c2226 0%,#2a3238 40%,#6c7a72 62%,#9aa49a 80%,#7d8a80 100%)}
.band-title{position:absolute;font-size:34px;line-height:41px;font-weight:900;color:#fff}
.band-text{position:absolute;font-size:14px;line-height:21px;color:#f2f2f2}
.welcome .btn,.features .btn{position:absolute;height:32px;line-height:32px;font-size:13px}

/* testimonials */
.testimonial{position:absolute;top:2745px;width:297px;height:374px;border:1px solid var(--line);text-align:center;background:#fff}
.quote-mark{position:absolute;top:22px;left:0;width:100%;font-family:Georgia,serif;font-size:56px;font-weight:700;color:var(--red);line-height:56px}
.stars{position:absolute;top:76px;width:100%;color:var(--red);font-size:17px;letter-spacing:1px}
.testimonial p{position:absolute;top:110px;left:38px;width:221px;font-size:13.5px;line-height:19.5px;color:var(--text)}
.avatar{position:absolute;top:272px;left:126px;width:44px;height:44px;border-radius:50%;background:linear-gradient(#b9b3ab,#8f877c)}
.testimonial .name{position:absolute;top:330px;width:100%;font-size:13px;color:var(--text)}
.arrow{position:absolute;top:2905px}

/* blog */
.blog{position:absolute;top:3176px;left:0;width:1200px;height:604px;background:var(--soft)}
.post{position:absolute;top:3320px;width:299px;height:417px;background:#fff}
.post .photo{position:absolute;left:0;top:0;width:299px;height:208px}
.post h4{position:absolute;top:236px;left:24px;width:222px;font-size:14px;line-height:19px;font-weight:800;color:var(--ink)}
.post p{position:absolute;top:283px;left:24px;width:250px;font-size:11px;line-height:16px;color:var(--muted)}
.post .btn{position:absolute;top:360px;left:24px;width:91px;height:24px;line-height:24px;font-size:10px}

.features{position:absolute;top:3780px;left:0;width:1200px;height:487px;background:linear-gradient(180deg,#3a3140 0%,#6a4a44 45%,#b06a3a 72%,#3b2a20 100%)}

/* footer */
.site-footer{position:absolute;top:4267px;left:0;width:1200px;height:370px;background:var(--black);color:#fff}
.site-footer .brand-name{left:128px;top:134px;font-size:24px;color:#fff}
.col-title{position:absolute;top:50px;font-family:"Nunito Sans",sans-serif;font-size:13px;font-weight:800}
.col-rule{position:absolute;top:74px;height:2px;background:#fff}
.contact-item{position:absolute;left:400px;font-size:11.5px;line-height:16px}
.contact-icon{position:absolute;left:-2px;top:2px;width:20px;height:20px;border-radius:50%;background:var(--red)}
.contact-item span{position:absolute;left:31px;white-space:nowrap}
.menu-list{position:absolute;left:711px;top:96px;font-size:11.5px;line-height:19.4px}
.social{position:absolute;left:956px;font-size:11px;line-height:15px}
.social i{position:absolute;left:0;top:1px;width:24px;height:24px;border-radius:50%;background:#fff}
.social span{position:absolute;left:36px;white-space:nowrap}
.footer-line{position:absolute;left:128px;top:4574px;width:934px;height:1px;background:#444}
.copyright{position:absolute;top:4601px;left:0;width:1200px;text-align:center;font-size:10px;color:#fff}
</style>
</head>
<body>

<header class="site-header">
  <div class="brand-name">Ridevolt Cycles</div>
  <nav class="main-nav">
    <span class="active" style="left:0">HOME</span>
    <span style="left:75px">ABOUT US</span>
    <span style="left:188px">SERVICES</span>
    <span style="left:287px">PRODUCTS</span>
    <span style="left:397px">BLOG</span>
    <span style="left:468px">CONTACT US</span>
  </nav>
  <svg class="cart" width="22" height="20" viewBox="0 0 22 20" fill="none" stroke="#151515" stroke-width="1.6"><path d="M1 2h3l3 11h11l2-8H6"/><circle cx="8.5" cy="17" r="1.5"/><circle cx="16.5" cy="17" r="1.5"/></svg>
  <div class="cart-badge">0</div>
</header>

<section class="hero" role="img" aria-label="Electric bicycle parked on a tree-lined paved path">
  <h1 class="hero-title">RESERVE THE PRODUCT WITH INTIAL PAYMENT OF $50</h1>
  <div class="hero-date">DECEMBER 25, 2023</div>
  <div class="countdown">
    <div class="digit">0</div><div class="digit">1</div>
    <div class="digit">1</div><div class="digit">4</div>
    <div class="digit">2</div><div class="digit">8</div>
    <div class="digit">0</div><div class="digit last">2</div>
  </div>
  <div class="count-labels">
    <span style="left:0">DAYS</span><span style="left:96px">HOURS</span>
    <span style="left:196px">MINUTES</span><span style="left:294px">SECONDS</span>
  </div>
  <span class="btn">PRE ORDER</span>
  <div class="dots"><i></i><i></i><i class="on"></i><i></i><i></i></div>
</section>

<h2 class="section-title" style="top:758px">OUR ELECTRIC BICYCLES</h2>
<div class="rule" style="left:578px;top:821px"></div>

<article class="product" style="left:131px;top:866px">
  <div class="photo" role="img" aria-label="Blue electric mountain bicycle" style="background:radial-gradient(ellipse at center,#9aa6d6 0%,#f4f3f3 70%)"></div>
  <h3>ELECTRIC BICYCLE 1</h3><div class="price">$874.00</div>
  <div class="swatches"><b>CHOOSE COLOUR</b><i style="background:#e8161b"></i><i style="background:#3b5bd6"></i><i style="background:#111"></i><i style="background:#7ab02a"></i></div>
  <p>Lorem ipsum dolor sit amet, consectetur adipiscing elit sed do eiusmod tempor incididunt ut labore et..</p>
  <span class="btn">SHOP NOW</span>
</article>
<article class="product" style="left:614px;top:866px">
  <div class="photo" role="img" aria-label="Black electric bicycle with orange rims" style="background:radial-gradient(ellipse at center,#c9b3a4 0%,#f4f3f3 70%)"></div>
  <h3>ELECTRIC BICYCLE 2</h3><div class="price">$950.00</div>
  <div class="swatches"><b>CHOOSE COLOUR</b><i style="background:#e8161b"></i><i style="background:#3b5bd6"></i><i style="background:#111"></i><i style="background:#7ab02a"></i></div>
  <p>Lorem ipsum dolor sit amet, consectetur adipiscing elit sed do eiusmod tempor incididunt ut labore et..</p>
  <span class="btn">SHOP NOW</span>
</article>
<article class="product" style="left:131px;top:1474px">
  <div class="photo" role="img" aria-label="Yellow electric mountain bicycle" style="background:radial-gradient(ellipse at center,#ddd08a 0%,#f4f3f3 70%)"></div>
  <h3>ELECTRIC BICYCLE 3</h3><div class="price">$874.00</div>
  <div class="swatches"><b>CHOOSE COLOUR</b><i style="background:#e8161b"></i><i style="background:#3b5bd6"></i><i style="background:#111"></i><i style="background:#7ab02a"></i></div>
  <p>Lorem ipsum dolor sit amet, consectetur adipiscing elit sed do eiusmod tempor incididunt ut labore et..</p>
  <span class="btn">SHOP NOW</span>
</article>
<article class="product" style="left:614px;top:1474px">
  <div class="photo" role="img" aria-label="Red electric city bicycle" style="background:radial-gradient(ellipse at center,#d89a9a 0%,#f4f3f3 70%)"></div>
  <h3>ELECTRIC BICYCLE 4</h3><div class="price">$950.00</div>
  <div class="swatches"><b>CHOOSE COLOUR</b><i style="background:#e8161b"></i><i style="background:#3b5bd6"></i><i style="background:#111"></i><i style="background:#7ab02a"></i></div>
  <p>Lorem ipsum dolor sit amet, consectetur adipiscing elit sed do eiusmod tempor incididunt ut labore et..</p>
  <span class="btn">SHOP NOW</span>
</article>

<section class="welcome" role="img" aria-label="Woman riding an electric bicycle through a city plaza">
  <h2 class="band-title" style="left:132px;top:52px">WELCOME TO<br>RIDEVOLT CYCLES</h2>
  <div class="rule" style="left:133px;top:148px"></div>
  <p class="band-text" style="left:133px;top:180px;width:468px">At vero eos et accusamus et iusto odio dignissimos ducimus qui blanditiis praesentium voluptatum deleniti atque corrupti quos dolores et quas molestias excepturi sint occaecati cupiditate non provident, similique sunt in culpa qui officia deserunt mollitia animi, id est laborum et dolorum fuga. Et harum quidem rerum facilis est et expedita distinctio. Nam libero tempore, cum soluta nobis est eligendi optio cumque nihil impedit quo minus id quod maxime placeat facere possimus, omnis voluptas assumenda est, omnis dolor repellendus. Temporibus autem quibusdam</p>
  <span class="btn" style="left:135px;top:399px;width:117px">READ MORE</span>
</section>

<h2 class="section-title" style="top:2645px">TESTIMONIALS</h2>
<div class="rule" style="left:578px;top:2707px"></div>
<svg class="arrow" style="left:70px" width="18" height="34" viewBox="0 0 18 34" fill="none" stroke="#777" stroke-width="2"><path d="M16 1 2 17l14 16"/></svg>
<svg class="arrow" style="left:1112px" width="18" height="34" viewBox="0 0 18 34" fill="none" stroke="#777" stroke-width="2"><path d="M2 1l14 16L2 33"/></svg>

<article class="testimonial" style="left:131px">
  <div class="quote-mark">“</div><div class="stars">★★★★★</div>
  <p>At vero eos et accusamus et iusto odio dignissimos ducimus qui blanditiis praesentium voluptatum deleniti atque corrupti quos dolores et quas molestias excepturi sint occa ecati cupiditate non provident, similique sunt in culpa qui officia deserunt mollitia anim.</p>
  <div class="avatar" role="img" aria-label="Customer portrait"></div><div class="name">Richard</div>
</article>
<article class="testimonial" style="left:451px">
  <div class="quote-mark">“</div><div class="stars">★★★★★</div>
  <p>At vero eos et accusamus et iusto odio dignissimos ducimus qui blanditiis praesentium voluptatum deleniti atque corrupti quos dolores et quas molestias excepturi sint occa ecati cupiditate non provident, similique sunt in culpa qui officia deserunt mollitia anim.</p>
  <div class="avatar" role="img" aria-label="Customer portrait"></div><div class="name">Richard</div>
</article>
<article class="testimonial" style="left:771px">
  <div class="quote-mark">“</div><div class="stars">★★★★★</div>
  <p>At vero eos et accusamus et iusto odio dignissimos ducimus qui blanditiis praesentium voluptatum deleniti atque corrupti quos dolores et quas molestias excepturi sint occa ecati cupiditate non provident, similique sunt in culpa qui officia deserunt mollitia anim.</p>
  <div class="avatar" role="img" aria-label="Customer portrait"></div><div class="name">Richard</div>
</article>

<section class="blog">
  <h2 class="section-title" style="top:36px">LATEST BLOG</h2>
  <div class="rule" style="left:578px;top:101px"></div>
</section>
<article class="post" style="left:132px">
  <div class="photo" role="img" aria-label="Woman standing with an electric bicycle on a city street" style="background:linear-gradient(160deg,#b9b08c,#7d8a62 60%,#a9a38e)"></div>
  <h4>SED UT PERSPICIATIS UNDE OMNIS ISTE NATUS</h4>
  <p>At vero eos et accusamus et iusto odio dignis simos ducimus qui blanditiis pra esentium voluptatum deleniti atque corrupti quos dolores et quos molestias.</p>
  <span class="btn">READ MORE</span>
</article>
<article class="post" style="left:450px">
  <div class="photo" role="img" aria-label="Close-up of hands fitting an electric bicycle battery" style="background:linear-gradient(160deg,#7f8a80,#3e4a42 55%,#6a7060)"></div>
  <h4>SED UT PERSPICIATIS UNDE OMNIS ISTE NATUS</h4>
  <p>At vero eos et accusamus et iusto odio dignis simos ducimus qui blanditiis pra esentium voluptatum deleniti atque corrupti quos dolores et quos molestias.</p>
  <span class="btn">READ MORE</span>
</article>
<article class="post" style="left:768px">
  <div class="photo" role="img" aria-label="Rider on an electric mountain bicycle in the hills" style="background:linear-gradient(180deg,#9fc2e0,#8ea48a 50%,#5d7a44)"></div>
  <h4>SED UT PERSPICIATIS UNDE OMNIS ISTE NATUS</h4>
  <p>At vero eos et accusamus et iusto odio dignis simos ducimus qui blanditiis pra esentium voluptatum deleniti atque corrupti quos dolores et quos molestias.</p>
  <span class="btn">READ MORE</span>
</article>

<section class="features" role="img" aria-label="Electric bicycle silhouetted against a sunset meadow">
  <h2 class="band-title" style="left:684px;top:82px">FEATURES &amp;<br>BENEFITS</h2>
  <div class="rule" style="left:686px;top:175px"></div>
  <p class="band-text" style="left:686px;top:205px;width:385px;font-size:15px;line-height:21px">At vero eos et accusamus et iusto odio dignissimos ducimus qui blanditiis praesentium voluptatum deleniti atque corrupti quos dolores et quas molestias excepturi sint occaecati cupiditate non provident, similique sunt in culpa qui officia deserunt mollitia animi, id est laborum et dolorum fuga.</p>
  <span class="btn" style="left:686px;top:380px;width:120px">READ MORE</span>
</section>

<footer class="site-footer">
  <div class="brand-name">Ridevolt Cycles</div>
  <div class="col-title" style="left:399px">CONTACT US</div>
  <div class="col-rule" style="left:399px;width:191px"></div>
  <div class="contact-item" style="top:102px"><i class="contact-icon"></i><span>418 Orchard Lane, Millbrook,<br>ON K0A 2B3, Canada</span></div>
  <div class="contact-item" style="top:151px"><i class="contact-icon"></i><span>Call Us<br>+1 555 014 2290</span></div>
  <div class="contact-item" style="top:202px"><i class="contact-icon"></i><span>E mail Us<br>hello@ridevolt-example.com</span></div>
  <div class="col-title" style="left:711px">MENU</div>
  <div class="col-rule" style="left:711px;width:105px"></div>
  <div class="menu-list">Home<br>About Us<br>Services<br>Products<br>Blog<br>Contact Us</div>
  <div class="col-title" style="left:958px">FOLLOW US</div>
  <div class="col-rule" style="left:958px;width:104px"></div>
  <div class="social" style="top:106px"><i></i><span>Like us on<br>FRIENDLINE</span></div>
  <div class="social" style="top:155px"><i></i><span>Follow us on<br>CHIRPNET</span></div>
  <div class="social" style="top:206px"><i></i><span>Follow us on<br>CLIPSTER</span></div>
</footer>
<div class="footer-line"></div>
<div class="copyright">Copyright © 2023 All Rights Reserved</div>

</body>
</html>
```